Luxury Brand Coffee Table Book Template

Overview:
We are creating a premium, 28-page coffee table book to accompany every bespoke jewelry piece handcrafted by Vellmoor Jewelry. This book serves as an heirloom that documents the story, design, and craftsmanship behind each custom piece, culminating in a powerful legacy statement. We need a refined, luxurious, and masculine layout template that can be updated for each new customer.
**All reference files (images, logos, copy for pages, etc.) are included in the .zip file.
Deliverables:
Print-ready 28-page InDesign or editable template file
Front and back cover design
Consistent typography and page layouts based on our outlined structure
Design system that allows for easy photo and text updates per client
Specs:
Size: 8.1 x 10.6 in, Portrait Orientation
Cover: Black linen hardcover with gold foil stamped name or crest (simulated in mockup)
Interior: Deep matte photo paper feel – minimalistic, clean layout with generous whitespace
Color Palette: Black, white, and gold
Style: Bold, masculine, timeless, high-luxury (think Karvane Studio x Dellbrook & Co.)
See the attached 28-page outline. Please use stock image placeholders for now.
Target Market(s)
Affluent Men & Women age 35-65
Industry/Entity Type
Luxury Retail Jewelry
Font styles to use
Other font styles liked:
- I really like Trajan Pro 3, but open to suggestions, as well as a mixture of Serif and Sans Serif fonts
Look and feel
Each slider illustrates characteristics of the customer's brand and the style your logo design should communicate.

```html
<!DOCTYPE html>
<html lang="en">
<head>
<meta charset="utf-8">
<title>Vellmoor Jewelry — Coffee Table Book Spreads</title>
<link rel="stylesheet" href="https://fonts.googleapis.com/css2?family=Cinzel:wght@400;500&family=EB+Garamond:wght@400;500&display=swap">
<style>
:root{
  --bg:#9a9a9c;
  --ink:#111111;
  --black:#000000;
  --white:#ffffff;
  --gold:#c9a23a;
  --red:#c1121f;
  --grey-band:#ededed;
  --cream:#f8ead2;
}
*{margin:0;padding:0;box-sizing:border-box}
html,body{width:1200px;height:3827px;overflow:hidden}
body{background:var(--bg);position:relative;font-family:"EB Garamond",Georgia,serif;color:var(--ink)}
h1,h2,h3{font-weight:400}
.page{position:absolute;overflow:hidden;box-shadow:0 4px 14px rgba(0,0,0,.28)}
.abs{position:absolute}
.body{font-size:10.6px;line-height:1.32;text-align:justify}
.placeholder{position:absolute}

/* cover */
.cover{left:600px;top:97px;width:536px;height:715px;background:var(--black)}
.brand{left:0;right:0;top:420px;display:flex;align-items:center;justify-content:center;gap:12px}
.brand-dot{width:40px;height:40px;border:2px solid var(--gold);border-radius:50%}
.brand-name{font-family:"Cinzel",serif;color:var(--gold);font-size:27px;font-weight:500;letter-spacing:.04em;line-height:1}

/* spread titles */
.spread-title{font-family:"Cinzel",serif;color:var(--white);font-size:17px;line-height:1.6;letter-spacing:.03em}

/* story page */
.story-band{left:428px;top:0;width:108px;height:465px;background:var(--grey-band)}
.story-vertical{left:425px;top:52px;font-family:"Cinzel",serif;font-size:92px;color:#d4d4d4;writing-mode:vertical-rl;transform:rotate(180deg);letter-spacing:.02em;line-height:1}
.index-num{font-family:"EB Garamond",serif;font-size:25px;color:var(--ink);text-align:center;line-height:1.1}
.index-label{font-family:"Cinzel",serif;font-size:9.5px;text-align:center;letter-spacing:.04em;margin-top:4px}
.index-item{position:absolute;top:640px;width:70px}

/* features */
.icon-box{position:absolute;border:1.5px solid #222;border-radius:8px;background:var(--white)}
.feature-title{font-family:"Cinzel",serif;font-size:11px;letter-spacing:.04em;margin-bottom:7px}

/* craft */
.step{position:absolute;width:210px}
.step-head{display:flex;align-items:baseline;gap:4px;margin-bottom:6px}
.step-num{font-family:"EB Garamond",serif;font-size:30px;color:#9c9c9c;line-height:1}
.step-title{font-family:"Cinzel",serif;font-size:16px;letter-spacing:.02em}
</style>
</head>
<body>

<!-- Cover -->
<section class="page cover">
  <div class="abs brand">
    <span class="brand-dot"></span>
    <span class="brand-name">VELLMOOR JEWELRY</span>
  </div>
</section>

<!-- Spread: story -->
<section class="page" style="left:64px;top:826px;width:536px;height:715px;background:var(--black)">
  <h2 class="abs spread-title" style="left:52px;top:96px">Hollis Darrow's Family Crest Ring:<br>A Legacy Forged in Trust</h2>
  <div class="abs" style="left:52px;top:165px;width:79px;height:3px;background:var(--red)"></div>
  <div class="placeholder" role="img" aria-label="Photograph of the gold, rose gold and enamel family crest ring on a black reflective surface"
       style="left:114px;top:175px;width:300px;height:430px;background:radial-gradient(ellipse at 55% 45%,#8a6a3a 0%,#4a3a22 40%,#111 75%,#000 100%)"></div>
</section>

<section class="page" style="left:600px;top:826px;width:536px;height:715px;background:var(--white)">
  <div class="abs story-band"></div>
  <div class="abs story-vertical">STORY</div>
  <h2 class="abs" style="left:33px;top:55px;font-family:'Cinzel',serif;font-size:24px">STORY</h2>
  <p class="abs body" style="left:33px;top:90px;width:340px;text-align:left">Every piece begins with a story - a powerful and inspirational idea with personal meaning that ignites the senses and captivates the audience</p>
  <h3 class="abs feature-title" style="left:33px;top:157px">A Symbol of Valor and Heritage</h3>
  <p class="abs body" style="left:33px;top:181px;width:340px">This Family Crest Ring honors Hollis Darrow, a distinguished Special Forces veteran whose life exemplifies courage, honor, and trust—the Darrow family motto: FIRMUS (“I Trust”). Crafted to celebrate both his Scottish lineage and his 20 years of exemplary military service, the ring tells Hollis’s unique story through powerful symbolism.</p>
  <div class="placeholder" role="img" aria-label="Photograph of a designer's desk with a whisky glass, a ring and a hand sketching with a pen, fading into white"
       style="left:0;top:270px;width:536px;height:380px;background:linear-gradient(180deg,#3c3a38 0%,#5a5650 45%,#8d8780 70%,#ffffff 100%)"></div>
  <div class="abs" style="left:428px;top:270px;width:108px;height:195px;background:rgba(237,237,237,.35)"></div>
  <h3 class="abs feature-title" style="left:33px;top:300px;color:var(--white)">Personal Note from Designer</h3>
  <p class="abs body" style="left:33px;top:326px;width:340px;color:var(--white)">Vellmoor Jewelry is an American fine jewelry brand renowned worldwide for its striking, evocative statement pieces. Our creations combine timeless craftsmanship with relentless innovation and meticulous detail, embodying the essence of luxury and valor.</p>
  <div class="abs" style="left:33px;top:660px;font-family:'Cinzel',serif;font-size:10px;letter-spacing:.04em">Contents Index</div>
  <div class="abs" style="left:33px;top:676px;width:126px;height:1px;background:var(--ink)"></div>
  <div class="index-item" style="left:159px"><div class="index-num">03</div><div class="index-label">Design</div></div>
  <div class="index-item" style="left:226px"><div class="index-num">08</div><div class="index-label">Craft</div></div>
  <div class="index-item" style="left:289px"><div class="index-num">16</div><div class="index-label">Legacy</div></div>
  <div class="index-item" style="left:357px"><div class="index-num">25</div><div class="index-label">Company</div></div>
  <div class="index-item" style="left:442px"><div class="index-num">27</div><div class="index-label">Biography</div></div>
</section>

<!-- Spread: design -->
<section class="page" style="left:64px;top:1555px;width:536px;height:715px;background:var(--white)">
  <div class="abs" style="left:0;top:0;width:536px;height:570px;background:var(--black)"></div>
  <h2 class="abs spread-title" style="left:82px;top:66px;font-size:14px;line-height:1.45">Hollis Darrow's Family Crest Ring:<br>A Legacy Forged in Trust</h2>
  <div class="abs" style="left:80px;top:120px;width:376px;height:452px;background:var(--white);border:3px solid var(--black);outline:2px solid var(--white)"></div>
  <div class="placeholder" role="img" aria-label="Grey pencil sketch of the crest: knight's helm over a chequy shield flanked by double-headed eagles and crossed arrows"
       style="left:100px;top:140px;width:336px;height:412px;background:radial-gradient(ellipse at 50% 45%,#bdbdbd 0%,#dedede 45%,#ffffff 80%)"></div>
  <h3 class="abs feature-title" style="left:82px;top:592px">A Symbol of Valor and Heritage</h3>
  <p class="abs body" style="left:82px;top:611px;width:376px">This Family Crest Ring honors Hollis Darrow, a distinguished Special Forces veteran whose life exemplifies courage, honor, and trust—the Darrow family motto: FIRMUS („I Trust”). Crafted to celebrate both his Scottish lineage and his 20 years of exemplary military service, the ring tells Hollis’s unique story through powerful symbolism.</p>
</section>

<section class="page" style="left:600px;top:1555px;width:536px;height:715px;background:var(--white)">
  <div class="icon-box" style="left:61px;top:90px;width:96px;height:85px">
    <div role="img" aria-label="Knight's helm" style="position:absolute;left:30px;top:16px;width:36px;height:52px;background:linear-gradient(#777,#222);border-radius:40% 40% 20% 20%"></div>
  </div>
  <div class="abs" style="left:181px;top:98px;width:300px">
    <h3 class="feature-title">Knight’s Helm: Guardian of Valor</h3>
    <p class="body" style="text-align:left">At the crest’s pinnacle, a Platinum Knight’s Helm symbolizes Hollis’s military valor, protection, and leadership, echoing the timeless honor of warriors past and present.</p>
  </div>
  <div class="icon-box" style="left:61px;top:234px;width:96px;height:82px">
    <div role="img" aria-label="Blue and red chequy shield" style="position:absolute;left:30px;top:12px;width:36px;height:56px;background:linear-gradient(#555 0 25%,#2b4fa8 25% 50%,#c22 50% 62%,#2b4fa8 62%);border-radius:0 0 50% 50%"></div>
  </div>
  <div class="abs" style="left:181px;top:241px;width:300px">
    <h3 class="feature-title">Scottish Shield: Heritage Reimagined</h3>
    <p class="body">The shield, enameled with museum-grade azure blue and a fess chequy Argent and Gules (silver-white and red squares), reflects the authentic Darrow family coat of arms. It honors Hollis’s Scottish ancestors who exemplified bravery and integrity through generations.</p>
  </div>
  <div class="icon-box" style="left:61px;top:390px;width:96px;height:85px">
    <svg width="96" height="85" viewBox="0 0 96 85" aria-label="Crossed arrows" role="img">
      <g stroke="#222" stroke-width="1.6" fill="none">
        <line x1="20" y1="28" x2="76" y2="57"/><line x1="76" y1="28" x2="20" y2="57"/>
        <polyline points="70,50 76,57 67,58"/><polyline points="26,50 20,57 29,58"/>
      </g>
    </svg>
  </div>
  <div class="abs" style="left:183px;top:398px;width:290px">
    <h3 class="feature-title">Crossed Arrows: Brotherhood and Courage</h3>
    <p class="body">Above the shield, platinum Crossed Arrows pay homage to Hollis’s service in the Allied Special Forces, symbolizing deep bonds of brotherhood, bravery, and trust forged on the battlefield.</p>
  </div>
  <div class="placeholder" role="img" aria-label="Dark close-up of the engraved crest with eagles and knight's helm"
       style="left:0;top:561px;width:536px;height:154px;background:radial-gradient(ellipse at 50% 40%,#4a4a4a 0%,#2a2a2a 55%,#1a1a1a 100%)"></div>
</section>

<!-- Spread: detailed sketches -->
<section class="page" style="left:64px;top:2284px;width:1072px;height:716px;background:var(--white)">
  <div class="abs" style="left:0;top:0;width:1072px;height:428px;background:var(--black)"></div>
  <h2 class="abs" style="left:52px;top:58px;font-family:'Cinzel',serif;color:var(--white);font-size:28px;line-height:1.2">Detailed<br>Sketches</h2>
  <div class="placeholder" role="img" aria-label="Full-colour illustration of the crest: golden double-headed eagles with name banners, knight's helm, blue shield with red and white chequy band, crossed arrows, rose gold filigree"
       style="left:188px;top:58px;width:698px;height:340px;background:radial-gradient(ellipse at 50% 50%,#2f7fd1 0%,#3a6fb0 14%,#c98a36 30%,#8a5a22 55%,#000 75%)"></div>

  <div class="icon-box" style="left:34px;top:466px;width:92px;height:80px">
    <div role="img" aria-label="Rose gold filigree shield frame" style="position:absolute;left:30px;top:12px;width:32px;height:56px;border:5px solid #a87262;border-radius:30% 30% 50% 50%"></div>
  </div>
  <div class="abs" style="left:147px;top:476px;width:340px">
    <h3 class="feature-title" style="font-size:10px;margin-bottom:4px">Rose Gold Filigree: Family Bonds</h3>
    <p class="body" style="text-align:left">The ring’s shield is framed by intricate 14k Rose Gold Filigree, representing familial love, unity, and the strength found in close-knit kinship.</p>
  </div>
  <div class="icon-box" style="left:34px;top:591px;width:92px;height:80px">
    <div role="img" aria-label="Golden double-headed eagle" style="position:absolute;left:22px;top:16px;width:48px;height:48px;background:radial-gradient(circle,#c8902c 0%,#7a4e16 70%,transparent 72%)"></div>
  </div>
  <div class="abs" style="left:147px;top:597px;width:340px">
    <h3 class="feature-title" style="font-size:10px;margin-bottom:4px">Double-Headed Eagles: Uniting Past and Future</h3>
    <p class="body">Cast in rich 14k Yellow Gold, twin double-headed eagles adorn each side, symbolizing a unified vision of past legacy and future aspirations. Banners on their chests proudly proclaim “DARROW” and the family motto “FIRMUS.”</p>
  </div>
  <div class="icon-box" style="left:572px;top:466px;width:92px;height:80px">
    <div role="img" aria-label="Hidden clan crest emblem" style="position:absolute;left:24px;top:12px;width:44px;height:56px;border:1.5px solid #222;border-radius:50%"></div>
  </div>
  <div class="abs" style="left:681px;top:470px;width:355px">
    <h3 class="feature-title" style="font-size:10px;margin-bottom:4px">Hidden Clan Crest: Inner Trust</h3>
    <p class="body" style="text-align:left">Inside the ring lies the private Darrow emblem—a Platinum Dexter Hand, a quiet, personal reminder of the clan’s historic gesture of trust. This hidden crest symbolizes Hollis’s internal commitment to family honor and integrity.</p>
  </div>
  <div class="icon-box" style="left:572px;top:591px;width:92px;height:80px">
    <div role="img" aria-label="Finished crest ring" style="position:absolute;left:26px;top:14px;width:40px;height:50px;background:radial-gradient(ellipse at 50% 35%,#3b5aa8 0%,#3b5aa8 30%,#b08a3a 40%,#5a4418 80%,transparent 82%)"></div>
  </div>
  <div class="abs" style="left:681px;top:597px;width:355px">
    <h3 class="feature-title" style="font-size:10px;margin-bottom:4px">A Ring of Lasting Legacy</h3>
    <p class="body">More than jewelry, Hollis Darrow’s custom crest ring is a testament to a life built on trust, valor, and family. It embodies his Scottish heritage, distinguished military service, and the enduring legacy he continues to forge.</p>
  </div>
</section>

<!-- Spread: craft -->
<section class="page" style="left:64px;top:3013px;width:1072px;height:714px;background:var(--white)">
  <div class="placeholder" role="img" aria-label="Photograph of an artisan's workbench with a gold coin pendant and a jar of polishing compound"
       style="left:0;top:0;width:536px;height:714px;background:radial-gradient(ellipse at 35% 75%,#8a7a5a 0%,#4a4640 35%,#2e2c2a 70%,#1e1d1c 100%)"></div>
  <div class="abs" style="left:389px;top:100px;width:147px;height:332px;background:rgba(120,90,60,.45)"></div>
  <div class="abs" style="left:420px;top:140px;font-family:'Cinzel',serif;font-size:58px;color:rgba(255,255,255,.42);writing-mode:vertical-rl;transform:rotate(180deg);line-height:1">CRAFT</div>
  <div class="abs" style="left:536px;top:70px;width:536px;height:362px;background:var(--cream)"></div>

  <div class="step" style="left:569px;top:103px"><div class="step-head"><span class="step-num">1</span><span class="step-title">Sculpt</span></div>
    <p class="body" style="text-align:left">Our seasoned jewelry engineers work closely with our expert sculptors to turn a 2-dimensional sketch into a 3-dimensional model - a beautiful marriage of art and science.</p></div>
  <div class="step" style="left:833px;top:103px"><div class="step-head"><span class="step-num">2</span><span class="step-title">Render</span></div>
    <p class="body" style="text-align:left">To complete phase 1, the design team will assign gemstone and precious materials to the model and use advanced software to generate realistic renderings of the jewelry.</p></div>
  <div class="step" style="left:569px;top:214px"><div class="step-head"><span class="step-num">3</span><span class="step-title">3D Print</span></div>
    <p class="body" style="text-align:left">Using cutting-edge 3D printers, we create wax molds. Many pieces contain thousands of layers in order to maintain every detail.</p></div>
  <div class="step" style="left:833px;top:214px"><div class="step-head"><span class="step-num">4</span><span class="step-title">Wax Prep</span></div>
    <p class="body" style="text-align:left">Our skilled artisans add the wax sprues - like branches of a tree, becoming a channel through which precious metal is poured into the mold.</p></div>
  <div class="step" style="left:569px;top:318px"><div class="step-head"><span class="step-num">5</span><span class="step-title">Invest</span></div>
    <p class="body" style="text-align:left">Wax trees are placed inside of a casting flask, which is filled with liquid gypsum and vibrated to release any bubbles, creating an air tight seal.</p></div>
  <div class="step" style="left:833px;top:318px"><div class="step-head"><span class="step-num">6</span><span class="step-title">Kiln</span></div>
    <p class="body" style="text-align:left">The flasks cook inside a kiln where the gypsum hardens as the wax melts away, resulting in a negative cavity for the metal to be poured into.</p></div>
  <div class="step" style="left:569px;top:449px"><div class="step-head"><span class="step-num">7</span><span class="step-title">Metals</span></div>
    <p class="body" style="text-align:left">Our goldsmith select only the finest and purest precious metals - gold, platinum, and silver - to use in our creations.</p></div>
  <div class="step" style="left:833px;top:449px"><div class="step-head"><span class="step-num">8</span><span class="step-title">Cast</span></div>
    <p class="body" style="text-align:left">Molten precious metal is poured into the investment mold, filling the cavities with and forming the jewelry piece.</p></div>
  <div class="step" style="left:569px;top:560px"><div class="step-head"><span class="step-num">9</span><span class="step-title">Assemble</span></div>
    <p class="body">Each individual casting must be removed, cleaned, delicately filed, and assembled to prepare for polishing.</p></div>
  <div class="step" style="left:833px;top:560px"><div class="step-head"><span class="step-num">10</span><span class="step-title">Polish</span></div>
    <p class="body">Through intense friction, rough outer layers are removed to reveal the brilliant design work and the jewelry begins to shine.</p></div>
</section>

</body>
</html>
```